Word Press Website design

Harborlight Studio is a Website design, SEO, Social Networking and app development company. We would like to see what you can do to create a new, relevant and exciting design for us. This is our first project for Pixel Meadow so we thought we would test drive this site.  We would like to leave it up to your creative interpretation of the new design, but you can checkout our old design at www.harborlightstudiohub.example
We are always looking for new talent for future projects. Wow us with your designs and there will be future work for you.

Target Market(s)
Our target customers are medium sized businesses of all vertical markets.
Industry/Entity Type
Internet
Font styles to use
Requirements
Must have
- Easy to navigate, HTML 5 sliders, modern
Nice to have
- Bring your graphic talents with an outside of the box design that will standout to prospective clients.

```html
<!DOCTYPE html>
<html lang="en">
<head>
<meta charset="utf-8">
<title>Harborlight Studio — Home</title>
<link rel="stylesheet" href="https://fonts.googleapis.com/css2?family=Open+Sans:ital,wght@0,400;0,600;0,700;1,400&family=Nothing+You+Could+Do&display=swap">
<style>
  :root {
    --ink: #222;
    --text: #5a5a5a;
    --muted: #8a8a8a;
    --accent: #3a98c6;
    --band: #8b8b8b;
    --paper: #fff;
    --hero-a: #f3f7fa;
    --hero-b: #cfdde7;
    --quote-bg: #eeeeee;
    --line: #d6d6d6;
    --footer: #2b2b2b;
    --footer-deep: #1f1f1f;
    --footer-text: #c9c9c9;
  }
  * { box-sizing: border-box; margin: 0; padding: 0; }
  html, body { width: 685px; height: 1200px; overflow: hidden; }
  body { position: relative; background: var(--paper); font-family: "Open Sans", Arial, sans-serif; color: var(--text); }
  .abs { position: absolute; }

  /* header */
  .site-header { position: absolute; left: 0; top: 0; width: 685px; height: 62px; }
  .header-band { position: absolute; left: 0; top: 46px; width: 685px; height: 13px; background: var(--band); }
  .brand { position: absolute; left: 67px; top: 6px; width: 143px; height: 54px; background: var(--paper); }
  .brand-name { position: absolute; left: 0; bottom: 0; width: 143px; height: 13px; background: #111; color: #fff; font-size: 8px; font-weight: 700; line-height: 13px; text-align: center; }
  .brand-mark { position: absolute; left: 4px; top: 6px; width: 14px; height: 14px; background: #333; }
  .brand-top { position: absolute; left: 24px; top: 8px; font-size: 12px; font-weight: 700; color: #222; }
  .main-nav { position: absolute; left: 217px; top: 18px; display: flex; gap: 17px; font-size: 7.4px; color: var(--muted); letter-spacing: .2px; }
  .main-nav .current { color: var(--ink); }

  /* hero slider */
  .hero { position: absolute; left: 0; top: 62px; width: 685px; height: 269px; background: radial-gradient(ellipse at 65% 55%, #fdfeff 0%, var(--hero-a) 35%, var(--hero-b) 100%); }
  .hero-title { position: absolute; left: 68px; top: 78px; font-size: 17.5px; line-height: 19px; color: var(--ink); }
  .hero-copy { position: absolute; left: 69px; top: 120px; width: 175px; font-size: 7.4px; line-height: 12.8px; color: var(--text); }
  .btn-dark { position: absolute; left: 69px; top: 176px; width: 59px; height: 20px; background: #3b3b3b; color: #fff; font-size: 7.2px; line-height: 20px; text-align: center; }
  .hero-visual { position: absolute; left: 256px; top: 18px; width: 340px; height: 236px; border-radius: 6px; background: linear-gradient(135deg, #2c3440 0%, #6e8ea3 45%, #d9e3ea 80%, #f7f9fb 100%); opacity: .85; }
  .slider-arrow { position: absolute; top: 125px; }

  /* services */
  .service { position: absolute; top: 368px; width: 120px; text-align: center; }
  .service svg { display: block; margin: 0 auto; }
  .service h3 { margin-top: 6px; font-size: 12px; font-weight: 400; color: var(--accent); }
  .service p { margin-top: 5px; font-size: 7.2px; line-height: 10.4px; color: var(--muted); }
  .btn-outline { display: inline-block; margin-top: 10px; width: 59px; height: 21px; border: 1px solid var(--line); font-size: 6.8px; line-height: 19px; color: var(--muted); }

  /* testimonial */
  .testimonials { position: absolute; left: 67px; top: 520px; width: 550px; height: 226px; background: var(--quote-bg); box-shadow: 0 6px 8px -6px rgba(0,0,0,.2); }
  .testimonials h2 { position: absolute; left: 0; top: 24px; width: 550px; text-align: center; font-family: "Nothing You Could Do", cursive; font-weight: 400; font-size: 17px; color: #555; }
  .quote-box { position: absolute; left: 31px; top: 63px; width: 490px; height: 91px; border: 1px solid #bdbdbd; background: var(--quote-bg); }
  .quote-box p { position: absolute; left: 52px; top: 13px; width: 398px; text-align: center; font-style: italic; font-size: 9.3px; line-height: 16.4px; color: #666; }
  .quote-mark { position: absolute; font-size: 30px; font-weight: 700; color: #666; line-height: 1; }
  .quote-tail { position: absolute; left: 238px; top: 90px; width: 11px; height: 11px; background: var(--quote-bg); border-right: 1px solid #bdbdbd; border-bottom: 1px solid #bdbdbd; transform: rotate(45deg); }
  .client-name { position: absolute; left: 190px; top: 174px; display: flex; align-items: center; gap: 4px; font-size: 14px; font-weight: 700; color: #1d2a5a; }
  .client-name span.sq { width: 12px; height: 12px; background: #3a7fc0; display: inline-block; }
  .client-meta { position: absolute; left: 275px; top: 174px; font-size: 7.4px; line-height: 11.5px; font-style: italic; color: var(--muted); }

  /* portfolio */
  .portfolio-title { position: absolute; left: 0; top: 788px; width: 685px; text-align: center; font-size: 24px; font-weight: 700; color: var(--accent); letter-spacing: .5px; }
  .portfolio-arrow { position: absolute; top: 800px; }
  .work { position: absolute; top: 832px; width: 128px; height: 127px; border: 1px solid var(--line); background: var(--paper); }
  .work .thumb { position: absolute; left: 3px; top: 2px; width: 122px; height: 91px; }
  .work span { position: absolute; left: 0; top: 103px; width: 126px; text-align: center; font-size: 7.6px; color: var(--muted); }

  /* footer */
  .site-footer { position: absolute; left: 0; top: 998px; width: 685px; height: 140px; background: var(--footer); color: var(--footer-text); }
  .footer-rule { position: absolute; top: 28px; width: 1px; height: 89px; background: #4a4a4a; }
  .footer-col h4 { position: absolute; font-size: 11.5px; font-weight: 400; color: #fff; }
  .contact-line { position: absolute; left: 71px; font-size: 7.2px; line-height: 11.5px; display: flex; gap: 6px; }
  .tweet { position: absolute; left: 230px; top: 44px; width: 140px; font-size: 7.2px; line-height: 11.6px; display: flex; gap: 6px; }
  .quick-links { position: absolute; left: 400px; top: 42px; list-style: none; font-size: 6.8px; line-height: 11.8px; }
  .quick-links li::before { content: "• "; }
  .quick-links .current { color: #fff; }
  .newsletter { position: absolute; left: 510px; top: 44px; width: 106px; height: 18px; background: #fff; border-radius: 2px; font-size: 6.6px; line-height: 18px; padding-left: 6px; color: var(--muted); }
  .newsletter-go { position: absolute; right: 0; top: 0; width: 24px; height: 18px; background: #d5d5d5; }
  .social { position: absolute; top: 1100px; width: 9px; height: 9px; border-radius: 50%; background: #777; }
  .footer-base { position: absolute; left: 0; top: 1138px; width: 685px; height: 62px; background: var(--footer-deep); color: #aaa; font-size: 6.6px; }
  .footer-base .copy { position: absolute; left: 70px; top: 18px; }
  .footer-base .links { position: absolute; left: 70px; top: 36px; }
</style>
</head>
<body>

<header class="site-header">
  <div class="header-band"></div>
  <div class="brand">
    <span class="brand-mark"></span>
    <span class="brand-top">Harborlight</span>
    <div class="brand-name">Harborlight Studio, Inc.</div>
  </div>
  <nav class="main-nav">
    <span class="current">HOME</span><span>ABOUT US</span><span>SERVICES</span><span>PORTFOLIO</span><span>CASE STUDIES</span><span>TESTIMONIALS</span><span>CONTACT US</span>
  </nav>
</header>

<section class="hero">
  <h1 class="hero-title" style="font-weight:400">Welcome to<br>Harborlight Studio, Inc.</h1>
  <p class="hero-copy">Harborlight Studio has been developing custom Websites in Riverton Bay since 1998. We build living, breathing, dynamic Website designs to meet the needs of diverse businesses.</p>
  <a class="btn-dark">READ MORE</a>
  <div class="hero-visual" role="img" aria-label="Desktop monitor with a cascade of floating website layouts"></div>
  <svg class="slider-arrow" style="left:12px" width="21" height="21" viewBox="0 0 21 21"><circle cx="10.5" cy="10.5" r="10.5" fill="#c4c9cd"/><path d="M12 6l-4.5 4.5L12 15" stroke="#fff" stroke-width="2.2" fill="none"/></svg>
  <svg class="slider-arrow" style="left:652px" width="21" height="21" viewBox="0 0 21 21"><circle cx="10.5" cy="10.5" r="10.5" fill="#c4c9cd"/><path d="M9 6l4.5 4.5L9 15" stroke="#fff" stroke-width="2.2" fill="none"/></svg>
</section>

<section class="services">
  <div class="service" style="left:71px">
    <svg width="30" height="26" viewBox="0 0 30 26"><rect x="1.5" y="1.5" width="27" height="23" rx="2" fill="none" stroke="#3a98c6" stroke-width="2"/><rect x="1.5" y="1.5" width="27" height="5" fill="#3a98c6"/><g fill="#3a98c6"><rect x="6" y="10" width="3" height="2"/><rect x="11" y="10" width="13" height="2"/><rect x="6" y="14" width="3" height="2"/><rect x="11" y="14" width="13" height="2"/><rect x="6" y="18" width="3" height="2"/><rect x="11" y="18" width="13" height="2"/></g></svg>
    <h3>Website Design</h3>
    <p>Proin placerat dapibus gravida.<br>In tristique tristique nulla eget hendrerit.</p>
    <a class="btn-outline">READ MORE</a>
  </div>
  <div class="service" style="left:212px">
    <svg width="30" height="26" viewBox="0 0 30 26"><rect x="2" y="4" width="20" height="20" rx="3" fill="none" stroke="#3a98c6" stroke-width="2"/><path d="M11 16l2-5 11-11 3 3-11 11z" fill="#fff" stroke="#3a98c6" stroke-width="2"/></svg>
    <h3>SEO</h3>
    <p>Proin placerat dapibus gravida.<br>In tristique tristique nulla eget hendrerit.</p>
    <a class="btn-outline">READ MORE</a>
  </div>
  <div class="service" style="left:353px">
    <svg width="30" height="26" viewBox="0 0 30 26"><path d="M3 9h6l13-7v20L9 15H3z" fill="#3a98c6"/><path d="M6 15l2 9h4l-2-9z" fill="#3a98c6"/><path d="M25 8a5 5 0 0 1 0 8" stroke="#3a98c6" stroke-width="2" fill="none"/></svg>
    <h3>Social Networking</h3>
    <p>Proin placerat dapibus gravida.<br>In tristique tristique nulla eget hendrerit.</p>
    <a class="btn-outline">READ MORE</a>
  </div>
  <div class="service" style="left:494px">
    <svg width="30" height="26" viewBox="0 0 30 26"><rect x="8" y="1" width="14" height="24" rx="2.5" fill="none" stroke="#3a98c6" stroke-width="2"/><rect x="11" y="5" width="8" height="14" fill="#3a98c6"/><circle cx="15" cy="22" r="1.2" fill="#3a98c6"/></svg>
    <h3>App Development</h3>
    <p>Proin placerat dapibus gravida.<br>In tristique tristique nulla eget hendrerit.</p>
    <a class="btn-outline">READ MORE</a>
  </div>
</section>

<section class="testimonials">
  <h2>What Our Clients Say About us....</h2>
  <div class="quote-box">
    <span class="quote-mark" style="left:18px;top:10px">&ldquo;</span>
    <p>Harborlight Studio did a great job on the development and implementation of our company's Website. The staff is extremely knowledgeable and explained everything thoroughly and in a language that a “Non-Technical” person would understand. The entire process went smoothly and the followed up support has been excellent.</p>
    <span class="quote-mark" style="left:452px;top:56px">&rdquo;</span>
    <div class="quote-tail"></div>
  </div>
  <div class="client-name"><span class="sq"></span>Brightleaf</div>
  <div class="client-meta">www.brightleafcatalog.example<br>President, Brightleaf Catalog</div>
</section>

<section class="portfolio">
  <svg class="portfolio-arrow" style="left:248px" width="8" height="12" viewBox="0 0 8 12"><path d="M6 1L2 6l4 5" stroke="#888" stroke-width="2" fill="none"/></svg>
  <h2 class="portfolio-title">PORTFOLIO</h2>
  <svg class="portfolio-arrow" style="left:428px" width="8" height="12" viewBox="0 0 8 12"><path d="M2 1l4 5-4 5" stroke="#888" stroke-width="2" fill="none"/></svg>
  <div class="work" style="left:68px"><div class="thumb" role="img" aria-label="Dark website layout with warm bokeh lights" style="background:linear-gradient(135deg,#2e2a24,#7a6a52 55%,#3a332a)"></div><span>Aliquam erat</span></div>
  <div class="work" style="left:208px"><div class="thumb" role="img" aria-label="Black website layout featuring a bicycle banner" style="background:linear-gradient(180deg,#1c2230 0%,#111 55%,#d8dadc 80%,#e9eaeb 100%)"></div><span>Aliquam erat</span></div>
  <div class="work" style="left:348px"><div class="thumb" role="img" aria-label="Retro greeting-card style website layout" style="background:linear-gradient(180deg,#8a7a6a 0%,#efe4cc 35%,#e6d8bb 75%,#6d9aa0 100%)"></div><span>Aliquam erat</span></div>
  <div class="work" style="left:488px"><div class="thumb" role="img" aria-label="Hands holding a transparent smartphone showing app icons" style="background:linear-gradient(135deg,#9fb6cf,#e8eef4 50%,#7c96b4)"></div><span>Aliquam erat</span></div>
</section>

<footer>
  <div class="site-footer">
    <div class="footer-rule" style="left:210px"></div>
    <div class="footer-rule" style="left:382px"></div>
    <div class="footer-rule" style="left:490px"></div>
    <div class="footer-col">
      <h4 style="left:71px;top:20px">Contact us</h4>
      <h4 style="left:230px;top:20px">Latest Tweet`s</h4>
      <h4 style="left:400px;top:20px">Quick Links</h4>
      <h4 style="left:511px;top:20px">Newsletter</h4>
      <h4 style="left:511px;top:73px">Follow us on</h4>
    </div>
    <div class="contact-line" style="top:46px"><svg width="7" height="9" viewBox="0 0 7 9"><path d="M3.5 0A3.2 3.2 0 0 0 .3 3.2C.3 5.6 3.5 9 3.5 9s3.2-3.4 3.2-5.8A3.2 3.2 0 0 0 3.5 0z" fill="#bbb"/><circle cx="3.5" cy="3.2" r="1.2" fill="#2b2b2b"/></svg><span>Address:<br>2470 Quayside Ave.<br>Riverton Bay, KS 66010</span></div>
    <div class="contact-line" style="top:85px"><svg width="8" height="8" viewBox="0 0 8 8"><path d="M1 0h2l1 2-1 1a5 5 0 0 0 2 2l1-1 2 1v2L7 8C3 8 0 5 0 1z" fill="#bbb"/></svg><span>Phone: 555-014-2290</span></div>
    <div class="contact-line" style="top:104px"><svg width="9" height="7" viewBox="0 0 9 7"><rect width="9" height="7" fill="#bbb"/><path d="M0 0l4.5 4L9 0" stroke="#2b2b2b" fill="none"/></svg><span>info@harborlightstudiohub.example</span></div>
    <div class="tweet"><svg width="8" height="7" viewBox="0 0 8 7"><path d="M0 1l4 2 4-3v5H0z" fill="#bbb"/></svg><span>Fusce vitae lectus sit amet mi pulvinar maximus<br>See more here<br>http://lnk.example/a8Kq2 Price USD skdfodsjfj http://lnk.example/b7Rt4<br>14 Jan</span></div>
    <ul class="quick-links"><li class="current">Home</li><li>About Us</li><li>Services</li><li>Portfolio</li><li>Case Studies</li><li>Testimonials</li></ul>
    <div class="newsletter">E-mail<span class="newsletter-go"><svg width="24" height="18" viewBox="0 0 24 18"><path d="M9 4l7 5-7 5z" fill="#888"/></svg></span></div>
  </div>
  <span class="social" style="left:511px" aria-label="Social network"></span>
  <span class="social" style="left:533px" aria-label="Social network"></span>
  <span class="social" style="left:554px" aria-label="Social network"></span>
  <div class="footer-base">
    <p class="copy">Copyright © 2014 by Northwind Web Co. All Rights Reserved.</p>
    <p class="links">Disclaimer &nbsp;|&nbsp; Support &nbsp;|&nbsp; Sitemap &nbsp;|&nbsp; Contact us</p>
    <svg class="abs" style="left:573px;top:22px" width="20" height="20" viewBox="0 0 20 20"><circle cx="10" cy="10" r="9" fill="none" stroke="#fff" stroke-width="1.6"/><rect x="5.5" y="7" width="9" height="6.5" fill="#fff"/><path d="M5.5 7l4.5 3.5L14.5 7" stroke="#1f1f1f" fill="none"/></svg>
    <svg class="abs" style="left:597px;top:22px" width="20" height="20" viewBox="0 0 20 20"><circle cx="10" cy="10" r="9" fill="none" stroke="#bbb" stroke-width="1.6"/><path d="M10 15V5M6 9l4-4 4 4" stroke="#bbb" stroke-width="1.6" fill="none"/></svg>
  </div>
</footer>

</body>
</html>
```